Powerpoint Presentation design template

I am looking for a PPT presentation that show class and professionalism and in the same colour them as the logo. It should be simple, but yet classy and pro. The business is an oil and gas exploration and exploitation business. The business has nothing to do with solar panel and other renewable energies, so please no solar panel or wind farms in the background. It would be more oil rigs and LNG plant in the background of some slide templates...

oil and gas exploration and exploitation

```html
<!DOCTYPE html>
<html lang="en">
<head>
<meta charset="utf-8">
<title>Kalemba Energy – Presentation Template</title>
<link href="https://fonts.googleapis.com/css2?family=Poppins:wght@400;600;700&family=Open+Sans:wght@400;600;700&family=Roboto:wght@400;500&display=swap" rel="stylesheet">
<style>
:root{
  --blue:#0a8ed6;
  --green:#55b92e;
  --teal:#12a37f;
  --ink:#141414;
  --text:#3a3a3a;
  --board:#b3b3b3;
  --band:#737373;
  --rule:#e6e6e6;
}
*{margin:0;padding:0;box-sizing:border-box}
html,body{width:1013px;height:1200px;overflow:hidden;background:var(--board)}
body{position:relative;font-family:"Open Sans",sans-serif;color:var(--text)}
.slide{position:absolute;width:459.5px;height:258.4px;overflow:hidden;background:#fff}
.col-l{left:31.6px}.col-r{left:521.5px}
.row-1{top:37.9px}.row-2{top:326.8px}.row-3{top:616.2px}.row-4{top:905.1px}
.frame{position:absolute;left:0;top:0;width:800px;height:450px;transform:scale(.5744);transform-origin:0 0}
.abs{position:absolute}
.slide-title{position:absolute;left:53px;top:14px;font-family:"Poppins",sans-serif;font-size:24px;color:var(--ink);font-weight:400;letter-spacing:.2px}
.slide-title b{font-weight:700}
.title-rule{position:absolute;left:53px;top:49px;width:90px;height:3px;background:var(--teal)}
.brand{position:absolute;right:55px;top:16px;display:flex;align-items:center;gap:7px}
.brand-dot{width:40px;height:40px;border-radius:50%;background:var(--blue)}
.brand-name{font-family:"Poppins",sans-serif;font-weight:700;color:var(--blue);line-height:1}
.brand-name .l1{display:block;font-size:21px}
.brand-name .l2{display:block;font-size:11px;letter-spacing:5.4px;margin-top:2px;padding-left:14px}
.footer-rule{position:absolute;left:0;top:406px;width:800px;height:1px;background:var(--rule)}
.footer{position:absolute;left:53px;right:53px;top:418px;display:flex;justify-content:space-between;font-size:10.5px;color:#333}
.footer .pg{font-size:9.5px}
.base-bar{position:absolute;left:0;bottom:0;width:800px;height:3px;background:linear-gradient(90deg,var(--blue),var(--teal))}
.body-copy{font-size:10.4px;line-height:14.6px;text-align:justify;color:var(--text)}
.body-copy p+p{margin-top:14.6px}
.wave-area{position:absolute;left:0;width:800px;background:linear-gradient(100deg,rgba(85,185,46,.85) 0%,rgba(85,185,46,.6) 45%,rgba(10,142,214,.75) 70%,rgba(10,142,214,.95) 100%)}
/* cover */
.cover{background:linear-gradient(180deg,#eef6f9 0%,#fafcfd 100%)}
.cover-photo{position:absolute;left:0;top:90px;width:800px;height:360px;background:linear-gradient(180deg,rgba(220,226,230,0) 0%,rgba(214,220,224,.7) 60%,rgba(230,233,235,.5) 100%)}
.cover .brand{right:auto;left:305px;top:44px}
.cover-title{position:absolute;left:0;width:800px;top:130px;text-align:center;font-family:"Poppins",sans-serif;font-weight:700;font-size:41px;color:var(--blue);letter-spacing:-.5px}
.cover-title span{color:var(--teal)}
.cover-sub{position:absolute;left:200px;width:400px;top:190px;text-align:center;font-size:10.5px;line-height:14.6px;color:#444}
.cover-est{position:absolute;left:0;width:800px;top:240px;text-align:center;font-family:"Poppins",sans-serif;font-weight:600;font-size:10px;color:var(--blue)}
/* agenda */
.agenda-disc{position:absolute;left:53px;top:101px;width:282px;height:282px;border-radius:50%;background:#0aae8a}
.agenda-photo{position:absolute;left:82px;top:130px;width:224px;height:222px;background:linear-gradient(160deg,#8fa8bf 0%,#c9d1d6 45%,#7e9a6a 100%)}
.agenda-item{position:absolute;left:399px;width:348px;height:36px}
.agenda-item .txt{position:absolute;left:0;top:11px;font-size:10.5px;font-weight:600;color:#222}
.agenda-item .line{position:absolute;left:1px;right:35px;top:34px;height:2px;background:#222}
.agenda-item .num{position:absolute;right:0;top:0;width:35px;height:36px;background:var(--blue);color:#fff;font-size:10.5px;display:flex;align-items:center;justify-content:center}
/* chart */
.chart-band{position:absolute;left:0;top:287px;width:800px;height:120px;background:var(--band)}
.chart-card{position:absolute;top:93px;width:332px;height:238px;background:#fff;box-shadow:0 0 4px rgba(0,0,0,.12)}
.chart-head{position:absolute;left:0;width:800px;top:342px;text-align:center;color:#fff;font-weight:700;font-size:17px}
.chart-note{position:absolute;left:110px;width:580px;top:368px;text-align:center;color:#fff;font-size:10.5px;line-height:14.6px}
/* services */
.service{position:absolute;top:170px;width:165px}
.service .ph{height:130px}
.service .cap{margin-top:9px;text-align:center;font-size:10.5px;font-weight:700;color:#222}
/* thank you */
.thanks{background:#f5f5f5}
.thanks-title{position:absolute;left:0;width:800px;top:52px;text-align:center;font-family:"Poppins",sans-serif;font-weight:700;font-size:41px;color:var(--ink)}
.thanks-rule{position:absolute;left:355px;top:118px;width:90px;height:3px;background:var(--green)}
.contact{position:absolute;top:150px;width:167px;height:118px;background:#fff;text-align:center;font-family:"Roboto",sans-serif;z-index:2}
.contact .ic{width:42px;height:42px;border-radius:50%;background:var(--green);margin:15px auto 12px;display:flex;align-items:center;justify-content:center}
.contact .lbl{font-size:10px;font-weight:500;color:#222}
.contact .val{font-size:8.5px;color:#333;margin-top:6px}
</style>
</head>
<body>

<!-- Cover -->
<section class="slide col-l row-1 cover"><div class="frame">
  <div class="cover-photo" role="img" aria-label="Faint refinery and LNG plant skyline in the background"></div>
  <div class="wave-area" style="top:300px;height:150px" role="img" aria-label="Green and blue curved wave decoration"></div>
  <div class="brand"><div class="brand-dot"></div><div class="brand-name"><span class="l1">KALEMBA</span><span class="l2">ENERGY</span></div></div>
  <h1 class="cover-title">KALEMBA <span>ENERGY</span></h1>
  <p class="cover-sub">Lorem ipsum dolor sit amet, consectetur adipiscing elit, sed do eiusmod tempor incididunt ut labore et dolore magna aliqua.</p>
  <p class="cover-est">ESTABLISHED IN 2020</p>
</div></section>

<!-- Text page -->
<section class="slide col-r row-1"><div class="frame">
  <h2 class="slide-title"><b>TITLE</b> HERE</h2><div class="title-rule"></div>
  <div class="brand"><div class="brand-dot"></div><div class="brand-name"><span class="l1">KALEMBA</span><span class="l2">ENERGY</span></div></div>
  <div class="body-copy abs" style="left:55px;top:92px;width:333px">
    <p>Lorem ipsum dolor sit amet, consectetur adipiscing elit, sed do eiusmod tempor incididunt ut labore et dolore magna aliqua. Ut enim ad minim veniam, quis nostrud exercitation ullamco laboris nisi ut aliquip ex ea commodo consequat. Duis aute irure dolor in reprehenderit in voluptate velit esse cillum dolore eu fugiat nulla pariatur. Excepteur sint occaecat cupidatat non proident, sunt in culpa qui officia deserunt mollit anim id est laborum.</p>
    <p>Sed ut perspiciatis unde omnis iste natus error sit voluptatem accusantium doloremque laudantium, totam rem aperiam, eaque ipsa quae ab illo inventore veritatis et quasi architecto beatae vitae dicta sunt explicabo. Nemo enim ipsam voluptatem quia voluptas sit aspernatur aut odit aut fugit, sed quia consequuntur magni dolores eos qui ratione voluptatem sequi nesciunt. Neque porro quisquam est, qui dolorem ipsum quia dolor sit amet, consectetur, adipisci velit, sed quia non numquam eius modi tempora incidunt ut labore et dolore magnam aliquam quaerat voluptatem. Ut enim ad minima veniam, quis nostrum exercitationem ullam corporis suscipit laboriosam, nisi ut aliquid ex ea commodi consequatur? Quis autem vel eum iure reprehenderit qui in ea voluptate velit</p>
  </div>
  <div class="body-copy abs" style="left:414px;top:92px;width:333px">
    <p>Lorem ipsum dolor sit amet, consectetur adipiscing elit, sed do eiusmod tempor incididunt ut labore et dolore magna aliqua. Ut enim ad minim veniam, quis nostrud exercitation ullamco laboris nisi ut aliquip ex ea commodo consequat. Duis aute irure dolor in reprehenderit in voluptate velit esse cillum dolore eu fugiat nulla pariatur. Excepteur sint occaecat cupidatat non proident, sunt in culpa qui officia deserunt mollit anim id est laborum.</p>
    <p>Sed ut perspiciatis unde omnis iste natus error sit voluptatem accusantium doloremque laudantium, totam rem aperiam, eaque ipsa quae ab illo inventore veritatis et quasi architecto beatae vitae dicta sunt explicabo. Nemo enim ipsam voluptatem quia voluptas sit aspernatur aut odit aut fugit, sed quia consequuntur magni dolores eos qui ratione voluptatem sequi nesciunt. Neque porro quisquam est, qui dolorem ipsum quia dolor sit amet, consectetur, adipisci velit, sed quia non numquam eius modi tempora incidunt ut labore et dolore magnam aliquam quaerat voluptatem. Ut enim ad minima veniam, quis nostrum exercitationem ullam corporis suscipit laboriosam, nisi ut aliquid ex ea commodi consequatur? Quis autem vel eum iure reprehenderit qui in ea voluptate velit</p>
  </div>
  <div class="footer-rule"></div>
  <div class="footer"><span>© Copyrights 2025 | All Rights Reserved</span><span class="pg">Page No : 05</span></div>
  <div class="base-bar"></div>
</div></section>

<!-- Agenda -->
<section class="slide col-l row-2"><div class="frame">
  <h2 class="slide-title"><b>AGENDA</b></h2><div class="title-rule"></div>
  <div class="brand"><div class="brand-dot"></div><div class="brand-name"><span class="l1">KALEMBA</span><span class="l2">ENERGY</span></div></div>
  <div class="agenda-disc"></div>
  <div class="agenda-photo" role="img" aria-label="Aerial view of an LNG storage tank terminal by the sea"></div>
  <div class="agenda-item" style="top:136px"><span class="txt">Lorem ipsum dolor sit amet, consectetur adipiscing elit</span><span class="line"></span><span class="num">01</span></div>
  <div class="agenda-item" style="top:190px"><span class="txt">Lorem ipsum dolor sit amet, consectetur adipiscing elit</span><span class="line"></span><span class="num">02</span></div>
  <div class="agenda-item" style="top:244px"><span class="txt">Lorem ipsum dolor sit amet, consectetur adipiscing elit</span><span class="line"></span><span class="num">03</span></div>
  <div class="agenda-item" style="top:298px"><span class="txt">Lorem ipsum dolor sit amet, consectetur adipiscing elit</span><span class="line"></span><span class="num">04</span></div>
  <div class="footer-rule"></div>
  <div class="footer"><span>© Copyrights 2025 | All Rights Reserved</span><span class="pg">Page No : 02</span></div>
  <div class="base-bar"></div>
</div></section>

<!-- Blank title page -->
<section class="slide col-r row-2"><div class="frame">
  <h2 class="slide-title"><b>TITLE</b> HERE</h2><div class="title-rule"></div>
  <div class="brand"><div class="brand-dot"></div><div class="brand-name"><span class="l1">KALEMBA</span><span class="l2">ENERGY</span></div></div>
  <div class="abs" style="left:268px;top:92px;width:264px;height:264px;border-radius:50%;background:linear-gradient(135deg,#f1f8ec,#eaf5fb)"></div>
  <div class="footer-rule"></div>
  <div class="footer"><span>© Copyrights 2025 | All Rights Reserved</span><span class="pg">Page No : 06</span></div>
  <div class="base-bar"></div>
</div></section>

<!-- About us -->
<section class="slide col-l row-3"><div class="frame">
  <h2 class="slide-title"><b>ABOUT</b> US</h2><div class="title-rule"></div>
  <div class="brand"><div class="brand-dot"></div><div class="brand-name"><span class="l1">KALEMBA</span><span class="l2">ENERGY</span></div></div>
  <div class="body-copy abs" style="left:55px;top:77px;width:694px">
    <p>Lorem ipsum dolor sit amet, consectetur adipiscing elit, sed do eiusmod tempor incididunt ut labore et dolore magna aliqua. Ut enim ad minim veniam, quis nostrud exercitation ullamco laboris nisi ut aliquip ex ea commodo consequat. Duis aute irure dolor in reprehenderit in voluptate velit esse cillum dolore eu fugiat nulla pariatur. Excepteur sint occaecat cupidatat non proident, sunt in culpa qui officia deserunt mollit anim id est laborum.</p>
    <p>Sed ut perspiciatis unde omnis iste natus error sit voluptatem accusantium doloremque laudantium, totam rem aperiam, eaque ipsa quae ab illo inventore veritatis et quasi architecto beatae vitae dicta sunt explicabo. Nemo enim ipsam voluptatem quia voluptas sit aspernatur aut odit aut fugit, sed quia consequuntur magni dolores eos qui ratione voluptatem sequi nesciunt. Neque porro quisquam est, qui dolorem ipsum quia dolor sit amet, consectetur, adipisci velit, sed quia non numquam eius modi tempora incidunt ut labore et dolore magnam aliquam quaerat voluptatem. Ut enim ad minima veniam, quis nostrum exercitationem ullam corporis suscipit laboriosam, nisi ut aliquid ex ea commodi consequatur? Quis autem vel eum iure reprehenderit qui in ea voluptate velit esse quam nihil molestiae consequatur, vel illum qui dolorem eum fugiat quo voluptas nulla pariatur</p>
    <p>Lorem ipsum dolor sit amet, consectetur adipiscing elit, sed do eiusmod tempor incididunt ut labore et dolore magna aliqua. Ut enim ad minim veniam, quis nostrud exercitation ullamco laboris nisi ut aliquip ex ea commodo consequat. Duis aute irure dolor in reprehenderit in voluptate velit esse cillum dolore eu fugiat nulla pariatur. Excepteur sint occaecat cupidatat non proident, sunt in culpa qui officia deserunt mollit anim id est laborum.</p>
    <p>Sed ut perspiciatis unde omnis iste natus error sit voluptatem accusantium doloremque laudantium, totam rem aperiam, eaque ipsa quae ab illo inventore veritatis et quasi architecto beatae vitae dicta sunt explicabo. Nemo enim ipsam voluptatem quia voluptas sit aspernatur aut odit aut fugit, sed quia consequuntur magni dolores eos qui ratione voluptatem sequi nesciunt.</p>
  </div>
  <div class="footer-rule"></div>
  <div class="footer"><span>© Copyrights 2025 | All Rights Reserved</span><span class="pg">Page No : 03</span></div>
  <div class="base-bar"></div>
</div></section>

<!-- Charts -->
<section class="slide col-r row-3"><div class="frame">
  <h2 class="slide-title"><b>TITLE</b> HERE</h2><div class="title-rule"></div>
  <div class="brand"><div class="brand-dot"></div><div class="brand-name"><span class="l1">KALEMBA</span><span class="l2">ENERGY</span></div></div>
  <div class="chart-band"></div>
  <div class="chart-card" style="left:53px">
    <svg width="332" height="238" viewBox="0 0 332 238" font-family="Open Sans, sans-serif" font-size="7" fill="#444">
      <g stroke="#eee" stroke-width="1"><line x1="22" y1="24" x2="325" y2="24"/><line x1="22" y1="48.5" x2="325" y2="48.5"/><line x1="22" y1="73" x2="325" y2="73"/><line x1="22" y1="97.5" x2="325" y2="97.5"/><line x1="22" y1="122" x2="325" y2="122"/><line x1="22" y1="146.5" x2="325" y2="146.5"/><line x1="22" y1="171" x2="325" y2="171"/><line x1="22" y1="195.5" x2="325" y2="195.5"/></g>
      <line x1="22" y1="220" x2="325" y2="220" stroke="#999"/>
      <g text-anchor="end"><text x="14" y="27">80</text><text x="14" y="51">70</text><text x="14" y="76">60</text><text x="14" y="100">50</text><text x="14" y="125">40</text><text x="14" y="149">30</text><text x="14" y="174">20</text><text x="14" y="198">10</text></g>
      <g fill="#0a8ed6"><rect x="34" y="97.5" width="14" height="122.5"/><rect x="70" y="97.5" width="14" height="122.5"/><rect x="110" y="171" width="14" height="49"/><rect x="146" y="97.5" width="14" height="122.5"/><rect x="185" y="48.5" width="14" height="171.5"/><rect x="221" y="97.5" width="14" height="122.5"/><rect x="259" y="97.5" width="14" height="122.5"/><rect x="295" y="122" width="14" height="98"/></g>
      <g fill="#7ed957"><rect x="52" y="73" width="14" height="147"/><rect x="128" y="146.5" width="14" height="73.5"/><rect x="203" y="73" width="14" height="147"/><rect x="277" y="48.5" width="14" height="171.5"/></g>
      <g text-anchor="middle" font-weight="700"><text x="59" y="230">2000</text><text x="135" y="230">2010</text><text x="210" y="230">2020</text><text x="284" y="230">2024</text></g>
    </svg>
  </div>
  <div class="chart-card" style="left:415px">
    <svg width="332" height="238" viewBox="0 0 332 238" font-family="Open Sans, sans-serif" font-size="7" fill="#444">
      <g stroke="#eee" stroke-width="1"><line x1="22" y1="24" x2="325" y2="24"/><line x1="22" y1="48.5" x2="325" y2="48.5"/><line x1="22" y1="73" x2="325" y2="73"/><line x1="22" y1="97.5" x2="325" y2="97.5"/><line x1="22" y1="122" x2="325" y2="122"/><line x1="22" y1="146.5" x2="325" y2="146.5"/><line x1="22" y1="171" x2="325" y2="171"/><line x1="22" y1="195.5" x2="325" y2="195.5"/></g>
      <line x1="22" y1="220" x2="325" y2="220" stroke="#999"/>
      <g text-anchor="end"><text x="14" y="27">80</text><text x="14" y="51">70</text><text x="14" y="76">60</text><text x="14" y="100">50</text><text x="14" y="125">40</text><text x="14" y="149">30</text><text x="14" y="174">20</text><text x="14" y="198">10</text></g>
      <g fill="#0a8ed6"><rect x="34" y="97.5" width="14" height="122.5"/><rect x="70" y="97.5" width="14" height="122.5"/><rect x="110" y="171" width="14" height="49"/><rect x="146" y="97.5" width="14" height="122.5"/><rect x="185" y="48.5" width="14" height="171.5"/><rect x="221" y="97.5" width="14" height="122.5"/><rect x="259" y="97.5" width="14" height="122.5"/><rect x="295" y="122" width="14" height="98"/></g>
      <g fill="#7ed957"><rect x="52" y="73" width="14" height="147"/><rect x="128" y="146.5" width="14" height="73.5"/><rect x="203" y="73" width="14" height="147"/><rect x="277" y="48.5" width="14" height="171.5"/></g>
      <g text-anchor="middle" font-weight="700"><text x="59" y="230">2000</text><text x="135" y="230">2010</text><text x="210" y="230">2020</text><text x="284" y="230">2024</text></g>
    </svg>
  </div>
  <h3 class="chart-head">Annual Revenues of $2 Million</h3>
  <p class="chart-note">Lorem ipsum dolor sit amet, consectetur adipiscing elit, sed do eiusmod tempor incididunt ut labore et dolore magna aliqua. Ut enim ad minim veniam, quis nostrud exercitation ullamco laboris nisi ut aliquip</p>
  <div class="footer-rule"></div>
  <div class="footer"><span>© Copyrights 2025 | All Rights Reserved</span><span class="pg">Page No : 07</span></div>
  <div class="base-bar"></div>
</div></section>

<!-- Services -->
<section class="slide col-l row-4"><div class="frame">
  <h2 class="slide-title"><b>OUR</b> SERVICES</h2><div class="title-rule"></div>
  <div class="brand"><div class="brand-dot"></div><div class="brand-name"><span class="l1">KALEMBA</span><span class="l2">ENERGY</span></div></div>
  <div class="body-copy abs" style="left:55px;top:90px;width:694px;text-align:left">
    <p>Lorem ipsum dolor sit amet, consectetur adipiscing elit, sed do eiusmod tempor incididunt ut labore et dolore magna aliqua. Ut enim ad minim veniam, quis nostrud exercitation ullamco laboris nisi ut aliquip ex ea commodo consequat. Duis aute irure dolor in reprehenderit in voluptate velit esse cillum dolore eu fugiat nulla pariatur. Excepteur sint occaecat cupidatat non proident, sunt in culpa qui officia deserunt mollit anim id est laborum.</p>
  </div>
  <div class="service" style="left:53px"><div class="ph" role="img" aria-label="Offshore oil rig lit at dusk" style="background:linear-gradient(180deg,#3f6f9c 0%,#c9867a 55%,#1d3f66 100%)"></div><p class="cap">Lorem ipsum dolor sit</p></div>
  <div class="service" style="left:229px"><div class="ph" role="img" aria-label="Oil pumpjacks at sunset" style="background:linear-gradient(180deg,#d9a36a 0%,#8a6a55 55%,#3a3b32 100%)"></div><p class="cap">Lorem ipsum dolor sit</p></div>
  <div class="service" style="left:405px"><div class="ph" role="img" aria-label="Offshore platform seen from a helicopter" style="background:linear-gradient(160deg,#2c4f6a 0%,#9a8740 50%,#d4a31e 100%)"></div><p class="cap">Lorem ipsum dolor sit</p></div>
  <div class="service" style="left:581px"><div class="ph" role="img" aria-label="Spherical LNG storage tanks" style="background:linear-gradient(180deg,#2f6fcf 0%,#c7d3e6 55%,#e3e6ea 100%)"></div><p class="cap">Lorem ipsum dolor sit</p></div>
  <div class="footer-rule"></div>
  <div class="footer"><span>© Copyrights 2025 | All Rights Reserved</span><span class="pg">Page No : 04</span></div>
  <div class="base-bar"></div>
</div></section>

<!-- Thank you -->
<section class="slide col-r row-4 thanks"><div class="frame">
  <div class="wave-area" style="top:300px;height:150px" role="img" aria-label="Green and blue curved wave decoration over a faint industrial skyline"></div>
  <h2 class="thanks-title">THANK YOU</h2>
  <div class="thanks-rule"></div>
  <div class="contact" style="left:134px"><div class="ic"><svg width="14" height="16" viewBox="0 0 14 16"><path d="M7,0 C3,0 1,3 1,6 C1,10 7,16 7,16 C7,16 13,10 13,6 C13,3 11,0 7,0 Z" fill="#fff"/><circle cx="7" cy="6" r="2.2" fill="#55b92e"/></svg></div><p class="lbl">Address :</p><p class="val">123, Lorem ipsum dolor sit</p></div>
  <div class="contact" style="left:317px"><div class="ic"><svg width="16" height="12" viewBox="0 0 16 12"><rect x="0" y="0" width="16" height="12" rx="1" fill="#fff"/><path d="M0,1 L8,7 L16,1" fill="none" stroke="#55b92e" stroke-width="1.4"/></svg></div><p class="lbl">Email Address :</p><p class="val">info@companyname.com</p></div>
  <div class="contact" style="left:499px"><div class="ic"><svg width="16" height="16" viewBox="0 0 16 16"><path d="M3,1 L6,1 L7,5 L5,6.5 C6,9 7,10 9.5,11 L11,9 L15,10 L15,13 C15,14 14,15 13,15 C6,15 1,10 1,3 C1,2 2,1 3,1 Z" fill="#fff"/></svg></div><p class="lbl">Phone :</p><p class="val">+1 888 888 8888</p></div>
</div></section>

</body>
</html>
```